電子書籍のタイトル

「窓辺に咲いた小さな灯と
心が旅をする十二の物語」

初めての出版になります。

基本デザインはお任せいたします。

デザインされる参考に添付内容の本文をお読みいください。

想定される読者の方の心に届く表紙にしたいと思います。

どうぞよろしくお願いいたします。

デザイン、文字の配置、色合いから総合的本の内容を表現されているように思いました。

この度は、表紙デザインにたくさんの方がご応募頂き誠にありがとうございました。
素晴らしい作品をたくさん頂き、正直悩みましたが、コンペという事で好みで選択させていただきました。本当に感謝申し上げます。

```html
<!DOCTYPE html>
<html lang="ja">
<head>
<meta charset="utf-8">
<title>窓辺に咲いた小さな灯と 心が旅をする十二の物語</title>
<link rel="stylesheet" href="https://fonts.googleapis.com/css2?family=M+PLUS+Rounded+1c:wght@500;700;800&family=Noto+Serif+JP:wght@700;900&family=Great+Vibes&display=swap">
<style>
  :root {
    --paper: #fbfcf4;
    --paper-edge: #eaf2d6;
    --band: #eef5dc;
    --leaf: #7cb52e;
    --leaf-deep: #5b9420;
    --ink: #3d3b2c;
    --white: #ffffff;
  }
  * { margin: 0; padding: 0; box-sizing: border-box; }
  html, body { width: 749px; height: 1200px; overflow: hidden; background: var(--paper); }
  .cover {
    position: relative;
    width: 749px; height: 1200px;
    overflow: hidden;
    background: radial-gradient(ellipse at 50% 42%, var(--white) 0%, var(--paper) 55%, var(--paper-edge) 100%);
    font-family: "M PLUS Rounded 1c", sans-serif;
    color: var(--ink);
    text-align: center;
  }
  .cover__band {
    position: absolute; left: 0; right: 0; top: 0; height: 100px;
    background: linear-gradient(180deg, var(--band), rgba(238,245,220,0));
  }
  .cover__frame {
    position: absolute; inset: 14px;
    border: 2px solid rgba(124,181,46,0.35);
    pointer-events: none;
  }
  .cover__orb {
    position: absolute;
    left: 95px; top: 180px;
    width: 560px; height: 560px;
    border-radius: 50%;
    background: radial-gradient(circle at 38% 34%, rgba(255,255,255,0.9) 0%, rgba(217,207,138,0.55) 35%, rgba(168,207,134,0.35) 62%, rgba(168,207,134,0) 72%);
    filter: blur(2px);
  }
  .title { position: absolute; left: 0; right: 0; top: 30px; }
  .title__lead {
    font-weight: 700; font-size: 37px; color: var(--leaf);
    letter-spacing: 0.04em; line-height: 1;
  }
  .title__rule {
    width: 660px; height: 2px; margin: 18px auto 0;
    background: linear-gradient(90deg, transparent, var(--leaf), transparent);
  }
  .title__main {
    display: block; margin-top: 34px;
    font-weight: 800; font-size: 84px; line-height: 1.15;
    letter-spacing: 0.02em;
    text-shadow: 0 0 10px var(--white), 0 0 4px var(--white);
  }
  .title__number {
    display: block; margin-top: 50px;
    font-family: "Noto Serif JP", serif; font-weight: 900;
    font-size: 150px; line-height: 1; color: var(--leaf);
    text-shadow: 0 0 12px var(--white);
  }
  .title__particle {
    display: block; margin-top: 20px;
    font-weight: 800; font-size: 56px; line-height: 1;
  }
  .title__tail {
    display: block; margin-top: 24px;
    font-weight: 800; font-size: 120px; line-height: 1; color: var(--leaf-deep);
    letter-spacing: 0.06em;
    text-shadow: 0 0 10px var(--white);
  }
  .author { position: absolute; left: 0; right: 0; top: 795px; }
  .author__role { font-weight: 700; font-size: 19px; letter-spacing: 0.06em; }
  .author__name {
    margin-top: 6px;
    font-family: "Great Vibes", cursive; font-size: 78px; line-height: 1;
  }
  .bonus {
    position: absolute; left: 30px; right: 30px; top: 1000px;
    padding: 34px 10px 18px;
    border-top: 2px solid var(--leaf);
    border-bottom: 2px solid var(--leaf);
  }
  .bonus__badge {
    position: absolute; left: 50%; top: -15px; transform: translateX(-50%);
    background: var(--leaf); color: var(--white);
    font-weight: 700; font-size: 15px; letter-spacing: 0.2em;
    padding: 5px 18px; border-radius: 14px; white-space: nowrap;
  }
  .bonus__line { font-weight: 700; font-size: 28px; line-height: 1.35; }
  .bonus__line--accent { font-size: 33px; color: var(--leaf-deep); }
</style>
</head>
<body>
  <main class="cover">
    <div class="cover__band"></div>
    <div class="cover__orb" role="img" aria-label="柔らかな光に包まれた円のイラスト"></div>
    <div class="cover__frame"></div>

    <header class="title">
      <p class="title__lead">窓辺に咲いた小さな灯と</p>
      <div class="title__rule"></div>
      <h1>
        <span class="title__main">心が旅をする</span>
        <span class="title__number">十二</span>
        <span class="title__particle">の</span>
        <span class="title__tail">物語</span>
      </h1>
    </header>

    <section class="author">
      <p class="author__role">心の灯をともす物語作家</p>
      <p class="author__name">Kazune</p>
    </section>

    <section class="bonus">
      <span class="bonus__badge">読者プレゼント</span>
      <p class="bonus__line">毎日をやわらかく照らすための心の習慣ノート</p>
      <p class="bonus__line bonus__line--accent">7つのひだまりレター</p>
    </section>
  </main>
</body>
</html>
```